Brindle Advisory Business Card Design

Business card for business consulting company, using attached logo. We do financial and strategic consulting, and want a clean, professional image with a bit of fun. Our logo is a flat whale tail, which symbolizes the Orca whale, a highly collaborative, group based animal that is very successful in navigating the ocean, protecting the herd, and hunting. We like the logo that is blue and gray on white one one side, but would be open to a blue card with white lettering on the other side... or whatever you'd suggest
Updates
Hi all - I have had the logo modified to take the shadowing off the tail. I will post it on the brief... under a file name called updated logo. thank you Added Saturday, April 25, 2015
Target Market(s)
Small to medium sized businesses ($10M to $500M in revenue per year), financial and sales executives, general managers, attorneys and CPAs
Industry/Entity Type
Financial
Contact Information for Business Card
Want company name, contact info - name, title, telephone, email, website, linkedin, twitter and Facebook. No physical address yet.
Requirements
Must have
- contemporary design, bold, strong, confident but with a bit of fun. prominently feature the logo and the whale tail icon
Nice to have
- unique touches that would differentiate us from a regular card... for example, logo and writing all on front on white background, but on back - logo in white on a blue background
- open to idea of different shapes of card than standard... but not sure
Should not have
- ?

```html
<!DOCTYPE html>
<html lang="en">
<head>
<meta charset="utf-8">
<title>Brindle Advisory – Business Card</title>
<link rel="stylesheet" href="https://fonts.googleapis.com/css2?family=Open+Sans:wght@400;600;700&display=swap">
<style>
  :root {
    --brand-blue: #0d56a8;
    --brand-blue-deep: #0a4791;
    --mark-blue: #1d4a86;
    --paper: #ffffff;
    --ink: #111111;
    --muted: #a9a9ad;
    --watermark: #c9c9d1;
    --backdrop: #e6e6e8;
    --logo-light: #b4b4b8;
  }
  * { box-sizing: border-box; margin: 0; padding: 0; }
  html, body {
    width: 1200px;
    height: 1152px;
    overflow: hidden;
    background: var(--backdrop);
    font-family: "Open Sans", sans-serif;
  }
  .sheet {
    position: relative;
    width: 1200px;
    height: 1152px;
  }
  .card {
    position: absolute;
    top: 190px;
    width: 440px;
    height: 770px;
    overflow: hidden;
    box-shadow: 0 6px 18px rgba(0,0,0,0.18);
  }

  /* Front */
  .card--front { left: 150px; background: var(--paper); }
  .front__band {
    position: absolute;
    left: 20px; top: 0;
    width: 84px; height: 100%;
    background: var(--brand-blue);
  }
  .front__logo {
    position: absolute;
    left: 20px; top: 60px;
    width: 84px;
    display: flex;
    flex-direction: column;
    align-items: center;
    gap: 16px;
  }
  .logo-name {
    writing-mode: vertical-rl;
    transform: rotate(180deg);
    font-weight: 600;
    white-space: nowrap;
    line-height: 1;
  }
  .front__logo .logo-name {
    font-size: 44px;
    color: var(--paper);
    letter-spacing: -1px;
  }
  .logo-tagline {
    writing-mode: vertical-rl;
    transform: rotate(180deg);
    font-size: 13px;
    white-space: nowrap;
  }
  .front__logo .logo-tagline { color: #dbe6f4; }
  .front__logo .logo-row {
    display: flex;
    flex-direction: row;
    align-items: flex-end;
    gap: 4px;
  }
  .logo-square {
    border-radius: 8px;
    background: var(--mark-blue);
  }
  .front__logo .logo-square { width: 56px; height: 56px; }

  .front__watermark {
    position: absolute;
    left: 150px; top: 270px;
    width: 360px; height: 400px;
    border-radius: 60px;
    background: var(--watermark);
    opacity: 0.55;
  }
  .front__header {
    position: absolute;
    left: 148px; top: 118px;
  }
  .person-name {
    font-size: 30px;
    font-weight: 400;
    color: var(--ink);
    line-height: 1.1;
  }
  .person-title {
    font-size: 17px;
    color: var(--muted);
    margin-left: 42px;
  }
  .contact {
    position: absolute;
    left: 210px; top: 420px;
    font-size: 16px;
    color: var(--ink);
    line-height: 1.4;
  }
  .contact dt { display: inline; font-weight: 700; }
  .contact dd { display: inline; }
  .contact .group { margin-bottom: 14px; }
  .contact p { margin: 0; }

  /* Back */
  .card--back {
    left: 610px;
    background: linear-gradient(160deg, var(--brand-blue) 0%, var(--brand-blue-deep) 100%);
  }
  .back__logo {
    position: absolute;
    left: 150px; top: 40px;
    display: flex;
    flex-direction: row;
    align-items: flex-end;
    gap: 6px;
  }
  .back__logo .logo-stack {
    display: flex;
    flex-direction: column;
    align-items: center;
    gap: 22px;
  }
  .back__logo .logo-name {
    font-size: 84px;
    color: var(--logo-light);
    letter-spacing: -2px;
  }
  .back__logo .logo-square { width: 128px; height: 118px; border-radius: 12px; }
  .back__logo .logo-tagline {
    font-size: 26px;
    color: var(--mark-blue);
    margin-bottom: 190px;
  }
</style>
</head>
<body>
<main class="sheet">

  <section class="card card--front" aria-label="Business card front">
    <div class="front__band"></div>
    <div class="front__logo">
      <div class="logo-row">
        <span class="logo-name">brindleadvisory</span>
        <span class="logo-tagline">business consulting</span>
      </div>
      <div class="logo-square"></div>
    </div>

    <div class="front__watermark"></div>

    <header class="front__header">
      <h1 class="person-name">Your Name Here</h1>
      <p class="person-title">Managing Director</p>
    </header>

    <dl class="contact">
      <div class="group">
        <p>No : 18 Harlow Lane,</p>
        <p>London, EC2N 4PQ</p>
      </div>
      <div class="group">
        <p><dt>Tel :</dt> <dd>+44 (0) 207 555 0142</dd></p>
        <p><dt>Fax :</dt> <dd>+44 (0) 207 555 0198</dd></p>
        <p><dt>Mobile :</dt> <dd>+0 700 555 318</dd></p>
      </div>
      <div class="group">
        <p><dt>E-mail :</dt> <dd>yourname@brindlemail.com</dd></p>
        <p><dt>Web :</dt> <dd>www.brindleadvisory.net</dd></p>
      </div>
      <div class="group">
        <p><dt>Facebook :</dt> <dd>Brindle Advisory</dd></p>
        <p><dt>Linkedin :</dt> <dd>Brindle Advisory</dd></p>
        <p><dt>Twitter :</dt> <dd>Brindle Advisory</dd></p>
      </div>
    </dl>
  </section>

  <section class="card card--back" aria-label="Business card back">
    <div class="back__logo">
      <div class="logo-stack">
        <span class="logo-name">brindleadvisory</span>
        <div class="logo-square"></div>
      </div>
      <span class="logo-tagline">business consulting</span>
    </div>
  </section>

</main>
</body>
</html>
```